Meridian Dash add on sales tool2017

This will be a flyer to leave with our clients we just did work for. We want to entice them to use our other services over the next 30 days with a discount, money off etc. we will write in the special and the expiration date. I want the client to read the description and see a picture of the service they may want done.

Target Market(s)

Repeat clients

Industry/Entity Type

Cleaning Service

Font styles to use
Serif
Sans Serif

Colors
ec1f27
000000
b1b1b1

Requirements
Must have
• Call to action! look high end market, clients show we do 1st class work.
• Don't Waite
Nice to have
• Classy, quality, I'm open to using other pictures that may look better
Should not have
• Look like a typical carpet cleaners special flyer
• Not to look cluttered

```html
<!DOCTYPE html>
<html lang="en">
<head>
<meta charset="utf-8">
<title>Meridian Dash – 30 Day Special Offer Flyer</title>
<link href="https://fonts.googleapis.com/css2?family=Archivo+Black&family=Arimo:wght@400;700&display=swap" rel="stylesheet">
<style>
  :root {
    --brand-red: #ec1f27;
    --brand-black: #000000;
    --brand-grey: #b1b1b1;
    --backdrop: #e9e7e3;
    --carpet-light: #c9b59a;
    --carpet-dark: #9c8769;
    --offer-box: #999999;
    --text-light: #f2f2f2;
    --body-on-red: #f6d2d3;
  }
  * { box-sizing: border-box; margin: 0; padding: 0; }
  html, body { width: 1200px; height: 900px; overflow: hidden; }
  body {
    background: var(--backdrop);
    font-family: "Arimo", Arial, sans-serif;
    position: relative;
  }
  .flyer {
    position: absolute;
    left: 270px; top: 22px;
    width: 660px; height: 856px;
    overflow: hidden;
    box-shadow: 0 6px 18px rgba(0,0,0,.25);
  }
  .flyer__backdrop {
    position: absolute; inset: 0;
    background: radial-gradient(ellipse at 40% 45%, var(--carpet-light), var(--carpet-dark));
  }
  .header {
    position: absolute; left: 120px; top: 0;
    width: 512px; height: 166px;
    background: linear-gradient(90deg, #2b2b2b 0%, #0d0d0d 35%, var(--brand-black) 60%);
    color: var(--text-light);
  }
  .brand {
    position: absolute; left: 44px; top: 46px;
    display: flex; align-items: center; gap: 8px;
    font-family: "Arimo", Arial, sans-serif; font-weight: 700;
    font-size: 15px; color: var(--brand-red); text-transform: uppercase;
  }
  .brand__mark { width: 12px; height: 12px; border-radius: 50%; background: var(--brand-red); }
  .header__cta {
    position: absolute; left: 44px; top: 104px;
    font-weight: 700; font-size: 19px; color: #d9d9d9;
  }
  .header__address {
    position: absolute; left: 44px; top: 126px;
    font-size: 12.5px; line-height: 15px; color: #e6e6e6;
  }
  .offer__title {
    position: absolute; left: 254px; top: 14px;
    font-weight: 700; font-size: 17px; letter-spacing: .3px; color: #e0e0e0;
  }
  .offer__box {
    position: absolute; left: 257px; top: 38px;
    width: 227px; height: 112px; background: var(--offer-box);
  }
  .offer__expires {
    position: absolute; left: 6px; bottom: 6px;
    font-size: 12px; color: var(--brand-black);
  }
  .tagline-band {
    position: absolute; left: 0; top: 166px;
    width: 660px; height: 38px;
    background: var(--brand-grey);
    display: flex; align-items: center; justify-content: center;
  }
  .tagline {
    font-family: "Archivo Black", "Arial Black", sans-serif;
    font-size: 22px; color: var(--brand-black);
    text-shadow: -1px -1px 0 #fff, 1px -1px 0 #fff, -1px 1px 0 #fff, 1px 1px 0 #fff, 2px 2px 2px rgba(0,0,0,.4);
    padding-left: 40px;
  }
  .services { position: absolute; left: 120px; top: 216px; width: 514px; }
  .service {
    position: relative; height: 123px; margin-bottom: 2px;
    display: flex;
    border-left: 6px solid var(--brand-red);
    filter: drop-shadow(3px 4px 3px rgba(0,0,0,.35));
  }
  .service__photo { width: 204px; height: 100%; position: relative; }
  .service__label {
    position: absolute; bottom: 4px;
    background: #fff; color: #1a237e; font-weight: 700;
    font-size: 10px; padding: 0 6px; line-height: 11px;
  }
  .service__panel {
    flex: 1; background: var(--brand-red);
    border-radius: 0 30px 30px 0;
    padding: 10px 16px 0 15px;
  }
  .service__title {
    font-family: "Archivo Black", "Arial Black", sans-serif;
    font-size: 17px; line-height: 20px; color: var(--brand-black);
    letter-spacing: .4px; margin-bottom: 6px;
  }
  .service__text {
    font-size: 11.5px; line-height: 14.7px; color: var(--body-on-red);
    max-width: 232px;
  }
</style>
</head>
<body>
<main class="flyer">
  <div class="flyer__backdrop" role="img" aria-label="Close-up photo of plush beige carpet with a living room armchair"></div>

  <header class="header">
    <div class="brand"><span class="brand__mark"></span>Meridian Dash</div>
    <p class="header__cta">Call now to book</p>
    <p class="header__address">4471 W. Calloway Ave. Suite C<br>Fairhaven</p>
    <p class="offer__title">30 DAY SPECIAL OFFER!</p>
    <div class="offer__box"><span class="offer__expires">Expires</span></div>
  </header>

  <div class="tagline-band"><h1 class="tagline">One Stop For All Your Home Cleaning Needs</h1></div>

  <section class="services">
    <article class="service">
      <div class="service__photo" role="img" aria-label="Photo of a freshly cleaned carpeted staircase" style="background:linear-gradient(160deg,#f2f0ec,#c9c5bd 60%,#8f8a82)"></div>
      <div class="service__panel">
        <h2 class="service__title">CARPET CLEANING</h2>
        <p class="service__text">Don't let dirty carpets spoil the look of your beautiful home!. with 37 years of cleaning carpets experience you can expect your carpets to look like new in most cases.</p>
      </div>
    </article>

    <article class="service">
      <div class="service__photo" role="img" aria-label="Before and after photo of an upholstered sofa being cleaned" style="background:linear-gradient(90deg,#8c8f86,#b5b8ad 50%,#c9cbbf 51%,#7d6a5a)">
        <span class="service__label" style="left:38px">Before</span>
        <span class="service__label" style="left:150px">After</span>
      </div>
      <div class="service__panel">
        <h2 class="service__title">UPHOLSTERY CLEANING</h2>
        <p class="service__text">Every day use leaves your sofa's and chairs lookng dingy and can smell like dog. Our Dry cleaning ,Shampoo or Rinse extraxtion will leave the fabric feel like clean sheet!</p>
      </div>
    </article>

    <article class="service">
      <div class="service__photo" role="img" aria-label="Photo of a technician cleaning drapes in a home" style="background:linear-gradient(90deg,#5a4a3e,#b8b6ad 45%,#6e6258)"></div>
      <div class="service__panel">
        <h2 class="service__title">DARAPERY CLEANING</h2>
        <p class="service__text">Drapery's act like a filter atracting atmisphiric soil! Making them look dingy, We make it easy to Dry clean in-home! Safe and efective beautiful drapery again.</p>
      </div>
    </article>

    <article class="service">
      <div class="service__photo" role="img" aria-label="Before and after photo of stone tile and grout cleaning" style="background:linear-gradient(90deg,#6f6c6b,#8c8886 50%,#b9ad9c 51%,#a79a88)">
        <span class="service__label" style="left:40px">Before</span>
        <span class="service__label" style="left:138px">After</span>
      </div>
      <div class="service__panel">
        <h2 class="service__title">TILE &amp; GROUT CLEANING</h2>
        <p class="service__text">Tile &amp; Grout get neglected! Dirty grout can leave permanent staining. Let our professionals bring back the look of a new floor.</p>
      </div>
    </article>

    <article class="service">
      <div class="service__photo" role="img" aria-label="Photo of a polished marble floor in a bright room" style="background:linear-gradient(180deg,#e6e6e4,#a9a9a6 55%,#5f5f5c)"></div>
      <div class="service__panel">
        <h2 class="service__title">NATURAL STONE CLEANING &amp; POLISHING</h2>
        <p class="service__text">A dull stained Marble - Granite-Travertine and other Natural stone can be revitalized to look NEW again!</p>
      </div>
    </article>
  </section>
</main>
</body>
</html>
```